Chilli Sauce - Label for Chilli Sauce bottle

I want a design for my chilli sauce label. I have included an example from an existing product. The key features of a successful design are as follows:
1. It shows the supplier: Brisk Meadow Condiments or Brisk Meadow if a shorter label fits better.
2. We need to have space for the ingredients. We will add these after.
3. Simple is good, refer attached. It doesn't need to be a design/logo, but a great design would be wonderful.
4. Some ideas. Brisk Meadow at the top of the label. Chilli Sauce in the middle of the label. Made with local ingredients (optional). Contains chilli - believe it or not (optional or similar wording)

```html
<!DOCTYPE html>
<html lang="en">
<head>
<meta charset="utf-8">
<title>Brisk Meadow Chilli Sauce Label</title>
<link rel="stylesheet" href="https://fonts.googleapis.com/css2?family=Oswald:wght@300;400&family=Jost:wght@400&family=Open+Sans:wght@400;500&display=swap">
<style>
  :root {
    --page-bg: #ffffff;
    --label-bg: #eae8e5;
    --chilli-red: #e8412a;
    --rule-red: #ec8b7c;
    --ink-grey: #555555;
    --band-text: #ffffff;
  }
  * { margin: 0; padding: 0; box-sizing: border-box; }
  html, body {
    width: 1200px;
    height: 1200px;
    overflow: hidden;
    background: var(--page-bg);
  }
  .canvas {
    position: relative;
    width: 1200px;
    height: 1200px;
  }
  .label {
    position: absolute;
    left: 280px;
    top: 242px;
    width: 642px;
    height: 716px;
    background: var(--label-bg);
    box-shadow: 4px 6px 10px rgba(0, 0, 0, 0.14);
  }
  .supplier {
    position: absolute;
    top: 44px;
    left: 0;
    width: 100%;
    text-align: center;
    font-family: "Oswald", sans-serif;
    font-weight: 400;
    font-size: 58px;
    line-height: 1;
    letter-spacing: 1px;
    color: var(--ink-grey);
    text-transform: uppercase;
  }
  .divider {
    position: absolute;
    top: 158px;
    left: 52px;
    width: 538px;
    height: 36px;
  }
  .divider .rule {
    position: absolute;
    top: 17px;
    height: 2px;
    width: 226px;
    background: var(--rule-red);
  }
  .divider .rule--left { left: 0; }
  .divider .rule--right { right: 0; }
  .divider .pepper {
    position: absolute;
    left: 247px;
    top: 2px;
    width: 44px;
    height: 30px;
  }
  .product-name {
    position: absolute;
    top: 218px;
    left: 0;
    width: 100%;
    text-align: center;
    font-family: "Jost", sans-serif;
    font-weight: 400;
    font-size: 134px;
    line-height: 130px;
    color: var(--chilli-red);
    text-transform: uppercase;
  }
  .tagline {
    position: absolute;
    top: 522px;
    left: 0;
    width: 100%;
    text-align: center;
    font-family: "Open Sans", sans-serif;
    font-weight: 400;
    font-size: 22px;
    color: var(--ink-grey);
  }
  .warning-band {
    position: absolute;
    top: 597px;
    left: 0;
    width: 100%;
    height: 50px;
    background: var(--chilli-red);
    display: flex;
    align-items: center;
    justify-content: center;
    font-family: "Open Sans", sans-serif;
    font-weight: 500;
    font-size: 23px;
    letter-spacing: 1.3px;
    color: var(--band-text);
  }
</style>
</head>
<body>
  <main class="canvas">
    <section class="label">
      <h1 class="supplier">Brisk Meadow</h1>

      <div class="divider">
        <span class="rule rule--left"></span>
        <svg class="pepper" viewBox="0 0 44 30" aria-hidden="true">
          <path d="M36 8 C30 8 26 12 20 17 C14 22 7 24 2 23 C7 27 16 27 24 22 C31 18 36 14 37 11 Z" fill="var(--chilli-red)"/>
          <path d="M35 9 C37 6 39 4 42 3" stroke="#4e8a2f" stroke-width="2" fill="none" stroke-linecap="round"/>
        </svg>
        <span class="rule rule--right"></span>
      </div>

      <h2 class="product-name">Chilli<br>Sauce</h2>

      <p class="tagline">- Made with local ingredients -</p>

      <p class="warning-band">Contains chilli - believe it or not</p>
    </section>
  </main>
</body>
</html>
```